copper lantern website

We need a new website for our new business division. We are a sustainable design firm specializing in servicing the needs if architects and developers. We have a staff consisting of architects, engineers, and former contractors and we understand green must make sense.

Bottomline - the only sustainable and copper lantern solutions are those thatbare good for the environment and good for our clients bottom line.

Our company is copper lantern and we will send you a copy of our logo you will see our tagline. Is simple. sustainable. solutions. The play with the periods is that we believe their are simple sustainable solutions and we want to use the words together and possible let each stand alone to accentuate their individual meaning in regards to benefit to our clients.

We want a cool splash page with nich graphics and pictures then later pages to feature projects and design ideas.

Target Market(s)

Our target customers are architects, developers, and contractors who would need assistance with the design process for a VARN project or assisatnce with a building owner who wants to make tehir facilty more environmentally friendly and save energy costs at the same tiem.

Industry/Entity Type

Environment

Requirements
Must have
• Needs a construction look with an environmentally friendly surrounding that is pleasing to look at. Must appeal to the client not only as environmentally friendly but also a wise investment.
Nice to have
• Opportunity for a connection to Social networking including a blog.
Should not have
• A totally environmental building feel at whatever cost. We want to emphasize that it is possible to build environmental friendly and save you money over the life of your building

```html
<!DOCTYPE html>
<html lang="en">
<head>
<meta charset="utf-8">
<title>copper lantern</title>
<link href="https://fonts.googleapis.com/css2?family=Arimo:wght@400;700&display=swap" rel="stylesheet">
<style>
  :root {
    --page: #ffffff;
    --frame: #9a9a9a;
    --leaf-light: #c9e07a;
    --leaf-mid: #8fbf2a;
    --leaf-deep: #4f8a1c;
    --brand-green: #4c9a2a;
    --accent-green: #63a832;
    --dot-green: #b5c21a;
    --dot-active: #3c8e2e;
    --ink-heading: #5e5e5e;
    --ink-body: #9a9a9a;
    --nav-top: #2c2c2c;
    --nav-bottom: #0c0c0c;
    --nav-divider: #444444;
    --footer-top: #3a3a3a;
    --footer-bottom: #151515;
    --footer-text: #ffffff;
    --footer-rule: #d8d8d8;
    --rule: #cfcfcf;
    --arrow-disc: #6d6d6d;
    --social-tile: #7a7a7a;
  }
  * { box-sizing: border-box; margin: 0; padding: 0; }
  html, body { width: 1200px; height: 1159px; overflow: hidden; background: var(--page); }
  body { font-family: "Arimo", Arial, sans-serif; position: relative; }

  .site { position: absolute; inset: 0; border: 1px solid var(--frame); overflow: hidden; }

  .leaf-backdrop {
    position: absolute; left: 0; top: 0; width: 1200px; height: 560px;
    background:
      linear-gradient(180deg, rgba(255,255,255,0) 55%, #ffffff 97%),
      radial-gradient(ellipse at 8% 30%, var(--leaf-light) 0%, var(--leaf-mid) 45%, var(--leaf-deep) 100%);
  }

  .header-tab {
    position: absolute; left: 153px; top: 0; width: 318px; height: 110px;
    background: var(--page); border-top-right-radius: 34px;
  }
  .brand { position: absolute; left: 176px; top: 39px; display: flex; align-items: center; gap: 10px; }
  .brand-mark { width: 30px; height: 30px; background: var(--brand-green); }
  .brand-name { font-size: 31px; font-weight: 400; color: var(--brand-green); line-height: 1; letter-spacing: -0.5px; }

  .main-nav {
    position: absolute; left: 497px; top: 26px; width: 552px; height: 52px;
    border-radius: 8px; background: linear-gradient(180deg, var(--nav-top), var(--nav-bottom));
    display: flex;
  }
  .main-nav a {
    flex: 1; display: flex; align-items: center; justify-content: center;
    color: #fff; font-weight: 700; font-size: 16px; text-decoration: none;
    border-left: 1px solid var(--nav-divider);
  }
  .main-nav a:first-child { border-left: none; }

  .content-panel {
    position: absolute; left: 153px; top: 100px; width: 896px; height: 766px;
    background: var(--page); border-top-right-radius: 18px;
  }

  .hero-slider { position: absolute; left: 172px; top: 121px; width: 857px; height: 388px; }
  .hero-image {
    position: absolute; inset: 0;
    background: linear-gradient(160deg, #e4e7ea 0%, #c8cfd2 35%, #5f8c3a 55%, #3c6e22 70%, #d9dcdc 100%);
  }
  .slider-arrow {
    position: absolute; top: 302px; width: 70px; height: 70px; border-radius: 50%;
    background: radial-gradient(circle at 40% 35%, #9a9a9a, var(--arrow-disc) 70%);
    display: flex; align-items: center; justify-content: center;
  }
  .slider-arrow.prev { left: 192px; }
  .slider-arrow.next { left: 942px; }
  .slider-dots { position: absolute; left: 192px; top: 484px; display: flex; gap: 6px; }
  .slider-dots span { width: 21px; height: 21px; border-radius: 50%; background: var(--dot-green); }
  .slider-dots span.active { background: var(--dot-active); }

  .feature { position: absolute; top: 552px; }
  .feature h2 { font-size: 36px; font-weight: 700; color: var(--ink-heading); line-height: 44px; white-space: nowrap; }
  .feature p { font-size: 13px; line-height: 17px; color: var(--ink-body); margin-top: 17px; }
  .feature-simple { left: 173px; width: 270px; }
  .feature-simple h2 { text-align: center; padding-right: 20px; }
  .feature-sustainable { left: 476px; width: 232px; }
  .feature-solution { left: 762px; width: 232px; }
  .feature-solution h2 { padding-left: 45px; }

  .point-list { list-style: none; margin-top: 17px; }
  .point-list li {
    font-size: 13px; color: var(--ink-body); height: 22.6px; display: flex; align-items: flex-start; gap: 8px; white-space: nowrap;
  }
  .point-list svg { flex: none; margin-top: 2px; }

  .column-rule { position: absolute; top: 555px; width: 3px; height: 274px; background: var(--rule); }

  .read-more {
    position: absolute; top: 825px; width: 133px; height: 33px; border-radius: 7px;
    background: linear-gradient(180deg, var(--nav-top), var(--nav-bottom));
    color: #fff; font-weight: 700; font-size: 14px; text-decoration: none;
    display: flex; align-items: center; justify-content: center;
  }

  .site-footer {
    position: absolute; left: 0; top: 866px; width: 1200px; height: 293px;
    background: linear-gradient(180deg, var(--footer-top), var(--footer-bottom));
  }
  .footer-block { position: absolute; top: 32px; }
  .footer-block h3 { font-size: 16px; font-weight: 700; color: var(--accent-green); margin-bottom: 8px; }
  .footer-block ul { list-style: none; }
  .footer-block li {
    height: 25.7px; padding-top: 6px; font-size: 12px; color: var(--footer-text);
    border-bottom: 1px dashed var(--footer-rule); white-space: nowrap;
  }
  .footer-menu { left: 153px; width: 280px; }
  .footer-menu h3 { padding-left: 17px; }
  .footer-menu li { padding-left: 21px; }
  .footer-partners { left: 460px; width: 280px; }
  .footer-partners h3 { padding-left: 18px; }
  .footer-partners li { padding-left: 21px; font-weight: 700; }

  .social-links { position: absolute; left: 888px; top: 39px; display: flex; gap: 6px; }
  .social-links a { width: 31px; height: 31px; border-radius: 5px; background: var(--social-tile); display: block; }

  .grass-image {
    position: absolute; left: 752px; top: 104px; width: 315px; height: 189px;
    background: linear-gradient(180deg, rgba(120,190,40,0) 0%, rgba(120,190,40,0.55) 45%, #3f7d1a 100%);
  }
</style>
</head>
<body>
<div class="site">
  <div class="leaf-backdrop" role="img" aria-label="Close-up photograph of a green leaf with veins"></div>

  <div class="header-tab"></div>
  <div class="brand"><span class="brand-mark"></span><span class="brand-name">copper lantern</span></div>

  <nav class="main-nav">
    <a href="#">Home</a><a href="#">About Us</a><a href="#">Services</a><a href="#">Work</a><a href="#">Contact</a>
  </nav>

  <div class="content-panel"></div>

  <section class="hero-slider">
    <div class="hero-image" role="img" aria-label="Rendering of a green-roofed terraced building among white city towers"></div>
  </section>
  <a class="slider-arrow prev" href="#" aria-label="Previous slide">
    <svg width="36" height="28" viewBox="0 0 36 28"><path d="M2 14 L34 2 L26 14 L34 26 Z" fill="#222"/></svg>
  </a>
  <a class="slider-arrow next" href="#" aria-label="Next slide">
    <svg width="36" height="28" viewBox="0 0 36 28"><path d="M34 14 L2 2 L10 14 L2 26 Z" fill="#222"/></svg>
  </a>
  <div class="slider-dots"><span class="active"></span><span></span><span></span><span></span><span></span></div>

  <section class="feature feature-simple">
    <h2>Simple</h2>
    <ul class="point-list">
      <li><svg width="11" height="10" viewBox="0 0 11 10"><path d="M0 0 L11 5 L0 10 L3 5 Z" fill="#4c9a2a"/></svg>It is a long established fact that a reader</li>
      <li><svg width="11" height="10" viewBox="0 0 11 10"><path d="M0 0 L11 5 L0 10 L3 5 Z" fill="#4c9a2a"/></svg>It is a long established fact that a reader</li>
      <li><svg width="11" height="10" viewBox="0 0 11 10"><path d="M0 0 L11 5 L0 10 L3 5 Z" fill="#4c9a2a"/></svg>It is a long established fact that a reader</li>
      <li><svg width="11" height="10" viewBox="0 0 11 10"><path d="M0 0 L11 5 L0 10 L3 5 Z" fill="#4c9a2a"/></svg>It is a long established fact that a reader</li>
      <li><svg width="11" height="10" viewBox="0 0 11 10"><path d="M0 0 L11 5 L0 10 L3 5 Z" fill="#4c9a2a"/></svg>It is a long established fact that a reader</li>
      <li><svg width="11" height="10" viewBox="0 0 11 10"><path d="M0 0 L11 5 L0 10 L3 5 Z" fill="#4c9a2a"/></svg>It is a long established fact that a reader</li>
      <li><svg width="11" height="10" viewBox="0 0 11 10"><path d="M0 0 L11 5 L0 10 L3 5 Z" fill="#4c9a2a"/></svg>It is a long established fact that a reader</li>
      <li><svg width="11" height="10" viewBox="0 0 11 10"><path d="M0 0 L11 5 L0 10 L3 5 Z" fill="#4c9a2a"/></svg>It is a long established fact that a reader</li>
    </ul>
  </section>
  <div class="column-rule" style="left:455px"></div>

  <section class="feature feature-sustainable">
    <h2>Sustainable</h2>
    <p>Lorem Ipsum is simply dummy text of the printing and typesetting industry.Lorem Ipsum has been the industry's standard dummy text ever since the 1500s, when an unknown printer took a galley of type and scrambled it to make a type specimen book. It has survived not only five centuries, but also the leap into electronic typesetting, remaining essentially unchanged. It was popularised in the</p>
  </section>
  <div class="column-rule" style="left:740px"></div>

  <section class="feature feature-solution">
    <h2>Solution</h2>
    <p>Lorem Ipsum is simply dummy text of the printing and typesetting industry.Lorem Ipsum has been the industry's standard dummy text ever since the 1500s, when an unknown printer took a galley of type and scrambled it to make a type specimen book. It has survived not only five centuries, but also the leap into electronic typesetting, remaining essentially unchanged.</p>
  </section>

  <a class="read-more" href="#" style="left:308px">Read More »</a>
  <a class="read-more" href="#" style="left:594px">Read More »</a>
  <a class="read-more" href="#" style="left:901px">Read More »</a>

  <footer class="site-footer">
    <div class="grass-image" role="img" aria-label="Photograph of green grass blades rising from the bottom edge"></div>
    <div class="footer-block footer-menu">
      <h3>Menu:</h3>
      <ul>
        <li>Home</li><li>About Us</li><li>Services</li><li>Work</li><li>Gallery</li><li>Blog</li><li>Contact</li>
      </ul>
    </div>
    <div class="footer-block footer-partners">
      <h3>Partners:</h3>
      <ul>
        <li>Contrary to popular belief</li><li>Contrary to popular belief</li><li>Contrary to popular belief</li>
        <li>Contrary to popular belief</li><li>Contrary to popular belief</li><li>Contrary to popular belief</li>
        <li>Contrary to popular belief</li>
      </ul>
    </div>
    <div class="social-links">
      <a href="#" aria-label="Social network"></a>
      <a href="#" aria-label="Social network"></a>
      <a href="#" aria-label="News feed"></a>
      <a href="#" aria-label="Blog"></a>
    </div>
  </footer>
</div>
</body>
</html>
```